Business Card Design Project

I am looking for a minimal matte background/shiny (spot UV) ink monochromatic design with a splash of neon color.

the card should be 2 sided, logo only on one side - all info and possibly logo on the other.

My creative director described the colors he imagined for the design to be:
'it's a dark field, like charcoal or a really dark burgundy, or deep blue, shot through with a neon—but just a tiny bit of it. so a charcoal field with a laser-thin streak of electric lime, safety orange, or cobalt blue. really beautiful stuff.'

here are some samples of the types of cards I am trying to create:
http://www.snapvault.example/photos/dawnpress/4182736450/in/photostream -> Vornelle Lustre

http://www.snapvault.example/photos/dawnpress/3859201746/in/photostream -> Standard Coated (14pt/matte) with SPOT UV

http://www.snapvault.example/photos/dawnpress/3859201372/in/photostream/ -> Dense Orvane with Raised Ink

http://www.snapvault.example/photos/dawnpress/5128463907/in/photostream/ -> Standard Coated (14pt/matte) with SPOT UV

Here is my logo:
https://www.filecrate.example/s/qtrwx730pkd4zn/gulvane%20logotype%20final.ai

Here are the details for info:
Owen Carlisle Dray
email - owen@gulvane.example
mobile - 555 318 6724
web -
gulvane.example: inventive technology applications
gulvane-video.example: innovative video advertising

please let me know if there is anything at all that you need.

Target Market(s)

mid to large agencies that require interactive design and entrepreneurial/startup individuals/companies that need application development.

Industry/Entity Type

Safety

Requirements
Must have
• logo only on one side

```html
<!DOCTYPE html>
<html lang="en">
<head>
<meta charset="utf-8">
<title>Gulvane Business Card</title>
<link rel="stylesheet" href="https://fonts.googleapis.com/css2?family=Open+Sans:wght@300;400;600&display=swap">
<style>
  :root {
    --backdrop: #2a2624;
    --card-navy: #1d2742;
    --card-navy-deep: #131a2d;
    --pattern-navy: #22305a;
    --lime: #7cc433;
    --ink-white: #eef1f6;
    --ink-soft: #c9cfdb;
  }
  * { margin: 0; padding: 0; box-sizing: border-box; }
  html, body {
    width: 1200px; height: 716px; overflow: hidden;
    background: var(--backdrop);
    font-family: "Open Sans", Arial, sans-serif;
  }
  .stage {
    position: relative; width: 1200px; height: 716px;
    display: flex; align-items: center; justify-content: center; gap: 40px;
  }
  .card {
    position: relative; width: 520px; height: 297px;
    background: linear-gradient(150deg, var(--card-navy) 0%, var(--card-navy-deep) 100%);
    border-radius: 4px;
    box-shadow: 0 10px 30px rgba(0,0,0,0.45);
    overflow: hidden;
  }
  /* Front: logo side */
  .front-pattern {
    position: absolute; left: 30px; top: 0; width: 230px; height: 190px;
    background: radial-gradient(ellipse at 45% 40%, var(--pattern-navy) 0%, rgba(34,48,90,0.35) 55%, rgba(34,48,90,0) 75%);
  }
  .wordmark {
    display: flex; align-items: center; gap: 10px;
    font-weight: 600; letter-spacing: 0.28em; text-transform: uppercase;
  }
  .wordmark-mark { width: 10px; height: 10px; background: var(--lime); flex: none; }
  .front .wordmark {
    position: absolute; right: 34px; bottom: 38px;
    font-size: 24px; color: var(--lime);
  }
  /* Back: info side */
  .holder { position: absolute; left: 36px; top: 30px; }
  .holder-name { font-size: 19px; font-weight: 300; color: var(--lime); line-height: 1.2; }
  .holder-title { font-size: 13px; color: var(--ink-white); margin-top: 2px; }
  .back .wordmark {
    position: absolute; left: 36px; bottom: 48px;
    font-size: 24px; color: var(--ink-white);
  }
  .back .wordmark-mark { width: 7px; height: 20px; }
  .contact {
    position: absolute; left: 300px; top: 112px;
    color: var(--ink-white); font-size: 14px; line-height: 1.3;
  }
  .contact-direct { margin-bottom: 14px; }
  .site { margin-bottom: 12px; }
  .site-tagline {
    display: flex; align-items: center; gap: 6px;
    font-size: 11.5px; color: var(--ink-soft);
  }
  .site-tagline::before {
    content: ""; width: 2px; height: 9px; background: var(--lime);
  }
</style>
</head>
<body>
  <main class="stage">
    <section class="card front" aria-label="Card front">
      <div class="front-pattern" role="img" aria-label="Faint spot UV hexagon cluster decoration"></div>
      <div class="wordmark"><span class="wordmark-mark"></span><span>Gulvane</span></div>
    </section>

    <section class="card back" aria-label="Card back">
      <div class="holder">
        <p class="holder-name">Owen Carlisle Dray</p>
        <p class="holder-title">Founder &amp; CEO</p>
      </div>
      <div class="wordmark"><span class="wordmark-mark"></span><span>Gulvane</span></div>
      <div class="contact">
        <div class="contact-direct">
          <p>555 318 6724</p>
          <p>owen@gulvane.example</p>
        </div>
        <div class="site">
          <p>gulvane.example</p>
          <p class="site-tagline">inventive technology applications</p>
        </div>
        <div class="site">
          <p>gulvane-video.example</p>
          <p class="site-tagline">innovative video advertising</p>
        </div>
      </div>
    </section>
  </main>
</body>
</html>
```